"tide-LOOP." SoCal's Fishing Industry's single stop for the latest products, content, and services

Hi, looking for a website design for new LA based company called "tide-LOOP." Where we showcase all the latest and greatest products, services, and content in a highly visually appealing platform for all fishing manufacturers and service providers as they relate to the fishing community (manufactures and service providers pay for cost-tiered content exposure and marketing, free exposure for manufacturers and service providers will have affiliate marketing link at minimal content exposure). As well, looking to include an in-site blog, store-products, and media content such as articles, video edits, and fishing condition picture galleries. Visually, looking for a minimalist/clean/blocked/ filterable and visually captivating gallery. Looking for a color pallet with white-background, deep blue- primary, light gray- secondary, light sky blue- third. Style- cleanliness and structure of wirestack.example meets content like mkharborline.example.

Target Market(s)

Primary- Southern California/Southwest Fishing Community, Secondary- All other US Fishing Communities

Coding

Coded - Design and coding required

Number of Pages Required

5+ page

Font styles to use
Sans Serif

Colors
959595
86cfc6
cadf82
333333
0555a3

Requirements
Must have
• Fast loading, mobile friendly, Analytics page, email sign up link for emailed newsletter (that is not a full page pop-up but integrated into browse bar), integrated social media links, search bar, filter link, home page return link, minimalist and clean design. Formatted to product showcase website style- please see attached files for ideas for design format and word-logo.
Should not have
• No Clutter, No background advertisements, No long text scripts outside of products main page,

```html
<!DOCTYPE html>
<html lang="en">
<head>
<meta charset="utf-8">
<title>tide-LOOP. — Home</title>
<link href="https://fonts.googleapis.com/css2?family=Montserrat:wght@400;500;600;700&display=swap" rel="stylesheet">
<style>
:root{
  --blue:#0555a3;
  --teal:#86cfc6;
  --teal-deep:#5fb4b2;
  --gray:#959595;
  --dark:#333333;
  --ink:#444;
  --white:#fff;
}
*{box-sizing:border-box;margin:0;padding:0}
html,body{width:1200px;height:4110px;overflow:hidden}
body{font-family:'Montserrat',sans-serif;color:var(--ink);background:var(--white);position:relative}
.abs{position:absolute}
a{color:inherit;text-decoration:none}
.photo{position:absolute;border-radius:14px}
.btn{position:absolute;display:flex;align-items:center;justify-content:center;font-size:14px;font-weight:500;color:#fff;background:var(--gray)}
.btn.primary{background:var(--blue)}
.section-title{position:absolute;left:0;width:1200px;text-align:center;font-size:30px;font-weight:600}
.section-title::after{content:"";display:block;width:70px;height:3px;margin:22px auto 0;background:currentColor}

/* header */
.brand{left:110px;top:28px;font-size:28px;font-weight:600;color:var(--blue)}
.brand-dot{position:absolute;left:110px;top:14px;width:10px;height:10px;border-radius:50%;background:var(--blue)}
.top-bar{top:28px;right:112px;display:flex;align-items:center;gap:26px;white-space:nowrap}
.top-contact{display:flex;align-items:center;gap:8px;font-size:13.5px}
.ico{width:30px;height:30px;border-radius:50%;display:flex;align-items:center;justify-content:center}
.nav{top:88px;right:112px;display:flex;gap:34px;font-size:15px;font-weight:500;color:var(--dark)}
.nav .on{color:var(--blue)}

/* hero */
.hero{left:0;top:129px;width:1200px;height:540px}
.hero-title{left:112px;top:290px;font-size:46px;font-weight:700;color:#fff;letter-spacing:2px}
.hero-text{left:112px;top:372px;width:470px;font-size:16px;font-weight:500;color:#fff;line-height:28px}
.hero-btn{left:112px;top:455px;width:130px;height:46px;border:2px solid #fff;color:#fff;font-size:15px;font-weight:600;display:flex;align-items:center;justify-content:center}

/* about */
.about-title{left:112px;top:748px;font-size:29px;font-weight:600;color:var(--blue)}
.about-text{left:112px;top:818px;width:560px;font-size:13.5px;line-height:26px}
.about-text p+p{margin-top:6px}

/* services */
.card-circle{position:absolute;width:150px;height:150px;border-radius:50%;background:#fff;border:6px solid rgba(255,255,255,.55);background-clip:padding-box;display:flex;align-items:center;justify-content:center}
.svc-h{position:absolute;width:320px;text-align:center;font-size:19px;font-weight:600;color:#fff}
.svc-p{position:absolute;width:300px;text-align:center;font-size:14px;line-height:27px;color:#fff}

/* blog */
.post-h{position:absolute;width:301px;text-align:center;font-size:19px;font-weight:600;color:var(--dark)}
.post-p{position:absolute;width:301px;text-align:center;font-size:13.5px;line-height:22px}

/* products */
.prod{position:absolute;width:285px;height:321px;background:#fff;box-shadow:0 4px 12px rgba(0,0,0,.12)}
.prod .pic{position:absolute;left:62px;top:28px;width:160px;height:150px;border-radius:8px}
.prod h3{position:absolute;top:200px;width:100%;text-align:center;font-size:20px;font-weight:600;color:var(--blue)}
.prod p{position:absolute;top:240px;left:30px;width:225px;text-align:center;font-size:14px;line-height:24px}

/* footer */
.foot-h{position:absolute;top:3745px;font-size:17px;font-weight:700;color:#fff;letter-spacing:.5px}
.foot-h::after{content:"";display:block;width:50px;height:2px;background:#fff;margin-top:12px}
.foot-links{position:absolute;left:367px;top:3805px;list-style:none;color:#fff;font-size:15px;font-weight:600;line-height:31px}
.foot-links li::before{content:"> ";font-weight:400}
.f-row{position:absolute;left:562px;display:flex;gap:18px;color:#fff;font-size:14px;line-height:21px}
.f-row .ico{border:2px solid #fff;width:40px;height:40px;flex:none}
.field{position:absolute;height:38px;border:1px solid #fff;color:#fff;font-size:12px;padding:0 10px;display:flex;align-items:center}
.social{position:absolute;top:4052px;width:34px;height:34px;border:2px solid #fff;border-radius:50%}
</style>
</head>
<body>

<!-- header -->
<div class="brand-dot"></div>
<a class="abs brand" href="#">tide-LOOP.</a>
<div class="abs top-bar">
  <div class="top-contact" style="color:var(--blue);font-weight:600">
    <span class="ico" style="background:var(--blue)"><svg width="14" height="12" viewBox="0 0 14 12"><rect x="1" y="1" width="12" height="10" fill="none" stroke="#fff" stroke-width="1.6"/><path d="M1 1l6 5 6-5" fill="none" stroke="#fff" stroke-width="1.6"/></svg></span>info@tideloop.example
  </div>
  <div class="top-contact" style="color:var(--dark)">
    <span class="ico" style="background:var(--gray)"><svg width="14" height="14" viewBox="0 0 24 24"><path d="M6.6 10.8a15 15 0 006.6 6.6l2.2-2.2a1 1 0 011-.25 11 11 0 003.5.56 1 1 0 011 1V20a1 1 0 01-1 1A17 17 0 013 4a1 1 0 011-1h3.5a1 1 0 011 1 11 11 0 00.56 3.5 1 1 0 01-.25 1z" fill="#fff"/></svg></span>180 555 0142
  </div>
</div>
<nav class="abs nav">
  <a class="on" href="#">Home</a><a href="#">About Us</a><a href="#">Articles</a><a href="#">Services</a><a href="#">Blog</a><a href="#">Gallery</a><a href="#">Contact Us</a>
</nav>

<!-- hero -->
<div class="abs hero" role="img" aria-label="Photo of a smiling worker in a fish market hall" style="background:linear-gradient(120deg,#3c5363 0%,#6f8494 45%,#8aa0ad 60%,#3f5b70 100%)"></div>
<svg class="abs" style="left:0;top:580px" width="1200" height="100" viewBox="0 0 1200 100" preserveAspectRatio="none">
  <path d="M0 40 C300 95 700 95 1200 20 L1200 100 L0 100Z" fill="#fff"/>
  <path d="M0 40 C300 95 700 95 1200 20" fill="none" stroke="var(--blue)" stroke-width="6"/>
</svg>
<svg class="abs" style="left:28px;top:370px" width="30" height="56"><path d="M26 4L4 28l22 24" fill="none" stroke="#fff" stroke-width="3"/></svg>
<svg class="abs" style="left:1142px;top:370px" width="30" height="56"><path d="M4 4l22 24L4 52" fill="none" stroke="#fff" stroke-width="3"/></svg>
<h1 class="abs hero-title">TIDE-LOOP</h1>
<p class="abs hero-text">Nemo enim ipsam voluptatem quia voluptas sit aspernatur aut odit aut fugit.</p>
<a class="hero-btn abs" href="#">READ MORE</a>

<!-- about -->
<h2 class="abs about-title">About tide-LOOP.</h2>
<div class="abs about-text">
  <p>Nemo enim ipsam voluptatem quia voluptas sit aspernatur aut odit aut fugit, sed quia consequuntur magni dolores eos qui ratione voluptatem sequi nesciunt. Neque porro quisquam est, qui dolorem ipsum quia dolor sit amet.</p>
  <p>Ut enim ad minima veniam, quis nostrum exercitationem ullam corporis suscipit labo riosam, nisi ut aliquid ex ea commodi consequatur. Sed ut perspiciatis unde omnis iste natus error sit voluptatem accusantium.</p>
</div>
<a class="btn" href="#" style="left:112px;top:990px;width:118px;height:42px">Read More</a>
<div class="abs" style="left:732px;top:759px;width:356px;height:277px;background:var(--blue)"></div>
<div class="abs" role="img" aria-label="Video still of an angler holding a catch by the sea" style="left:690px;top:787px;width:375px;height:222px;background:linear-gradient(180deg,#8cc4e6 0%,#bfe0f2 45%,#2d7fb3 62%,#1e5f8c 100%)"></div>
<div class="abs" style="left:848px;top:868px;width:58px;height:58px;border-radius:50%;border:3px solid #fff;background:rgba(0,0,0,.25)"></div>
<svg class="abs" style="left:868px;top:884px" width="22" height="26"><path d="M2 2l18 11L2 24z" fill="#fff"/></svg>

<!-- services -->
<svg class="abs" style="left:0;top:1118px" width="1200" height="712" viewBox="0 0 1200 712" preserveAspectRatio="none" role="img" aria-label="Underwater backdrop with fish">
  <defs><linearGradient id="sea" x1="0" y1="0" x2="0" y2="1"><stop offset="0" stop-color="#6cc1bd"/><stop offset="1" stop-color="#4aa7ab"/></linearGradient></defs>
  <path d="M0 40 C250 0 420 60 700 30 C900 10 1050 10 1200 20 L1200 660 C1000 700 800 640 500 690 C300 720 150 680 0 700Z" fill="url(#sea)"/>
</svg>
<h2 class="section-title" style="top:1252px;color:#fff">Our Services</h2>
<div class="card-circle" style="left:172px;top:1363px"><svg width="70" height="70" viewBox="0 0 70 70"><circle cx="42" cy="26" r="20" fill="none" stroke="#555" stroke-width="2"/><path d="M28 40L8 64" stroke="#555" stroke-width="3"/></svg></div>
<div class="card-circle" style="left:525px;top:1363px"><svg width="70" height="70" viewBox="0 0 70 70"><path d="M20 15c20 0 30 10 25 25s-20 10-15 20" fill="none" stroke="#d05a6e" stroke-width="2.5"/><circle cx="20" cy="15" r="4" fill="none" stroke="#d05a6e" stroke-width="2"/></svg></div>
<div class="card-circle" style="left:878px;top:1363px"><svg width="70" height="70" viewBox="0 0 70 70"><path d="M6 56C30 20 50 14 66 16" fill="none" stroke="#444" stroke-width="3"/><circle cx="26" cy="42" r="6" fill="#444"/></svg></div>
<div class="svc-h" style="left:87px;top:1538px">NEMO ENIM IPSAM</div>
<div class="svc-h" style="left:440px;top:1538px">NEMO ENIM IPSAM</div>
<div class="svc-h" style="left:793px;top:1538px">NEMO ENIM IPSAM</div>
<p class="svc-p" style="left:97px;top:1577px">Sed ut perspiciatis unde omnis iste natus error sit voluptatem accusantium doloremque laudantium</p>
<p class="svc-p" style="left:450px;top:1577px">Sed ut perspiciatis unde omnis iste natus error sit voluptatem accusantium doloremque laudantium</p>
<p class="svc-p" style="left:803px;top:1577px">Sed ut perspiciatis unde omnis iste natus error sit voluptatem accusantium doloremque laudantium</p>
<svg class="abs" style="left:0;top:1670px" width="1200" height="30">
  <path d="M155 18c40-10 140-10 180 0" fill="none" stroke="#fff" stroke-width="4"/>
  <path d="M508 18c40-10 140-10 180 0" fill="none" stroke="#fff" stroke-width="4"/>
  <path d="M861 18c40-10 140-10 180 0" fill="none" stroke="#fff" stroke-width="4"/>
</svg>

<!-- blog -->
<h2 class="section-title" style="top:1893px;color:var(--blue)">Our Blog Posts</h2>
<div class="photo" role="img" aria-label="Photo of a parent and child fishing together" style="left:118px;top:2006px;width:301px;height:192px;background:linear-gradient(135deg,#7fa96a,#c8d6a2 50%,#5c8a4e)"></div>
<div class="photo" role="img" aria-label="Photo of an open tackle box with reels and lures" style="left:452px;top:2006px;width:301px;height:192px;background:linear-gradient(135deg,#4c5a68,#9aa6ad 50%,#3a4550)"></div>
<div class="photo" role="img" aria-label="Close-up photo of a fishing reel" style="left:784px;top:2006px;width:301px;height:192px;background:linear-gradient(135deg,#3d2f28,#a89281 50%,#2f2620)"></div>
<div class="post-h" style="left:118px;top:2236px">NEMO ENIM IPSAM</div>
<div class="post-h" style="left:452px;top:2236px">NEMO ENIM IPSAM</div>
<div class="post-h" style="left:784px;top:2236px">NEMO ENIM IPSAM</div>
<p class="post-p" style="left:118px;top:2270px">Sed ut perspiciatis unde omnis iste natus error sit voluptatem accusantium doloremquem.</p>
<p class="post-p" style="left:452px;top:2270px">Sed ut perspiciatis unde omnis iste natus error sit voluptatem accusantium doloremquem.</p>
<p class="post-p" style="left:784px;top:2270px">Sed ut perspiciatis unde omnis iste natus error sit voluptatem accusantium doloremquem.</p>
<a class="btn primary" href="#" style="left:216px;top:2344px;width:106px;height:40px">Read More</a>
<a class="btn" href="#" style="left:550px;top:2344px;width:106px;height:40px">Read More</a>
<a class="btn" href="#" style="left:882px;top:2344px;width:106px;height:40px">Read More</a>

<!-- store products -->
<svg class="abs" style="left:0;top:2460px" width="1200" height="710" viewBox="0 0 1200 710" preserveAspectRatio="none">
  <path d="M0 60 C200 0 400 30 600 40 C850 55 1000 0 1200 30 L1200 640 C1000 700 800 640 600 670 C400 700 200 640 0 660Z" fill="var(--teal)"/>
</svg>
<h2 class="section-title" style="top:2582px;color:#fff">Store Products</h2>
<div class="prod" style="left:112px;top:2704px"><div class="pic" role="img" aria-label="Product photo of a spool of fishing line" style="background:radial-gradient(circle,#eef0ea 20%,#9aa08a 45%,#f4f4f4 70%)"></div><h3>Totam Rem Aperiam</h3><p>Ut enim ad minima veniam, quis nos trum exercitationem.</p></div>
<div class="prod" style="left:457px;top:2704px"><div class="pic" role="img" aria-label="Product photo of a fishing rod handle with reel seat" style="background:linear-gradient(160deg,#f6f6f6 35%,#555 50%,#f6f6f6 65%)"></div><h3>Totam Rem Aperiam</h3><p>Ut enim ad minima veniam, quis nos trum exercitationem.</p></div>
<div class="prod" style="left:803px;top:2704px"><div class="pic" role="img" aria-label="Product photo of a spinning reel" style="background:radial-gradient(circle,#333 25%,#8a8a8a 40%,#f6f6f6 62%)"></div><h3>Totam Rem Aperiam</h3><p>Ut enim ad minima veniam, quis nos trum exercitationem.</p></div>

<!-- gallery -->
<h2 class="section-title" style="top:3244px;color:var(--blue)">Our Gallery</h2>
<div class="photo" role="img" aria-label="Photo of fishing gear on a forest riverbank" style="left:118px;top:3348px;width:301px;height:195px;background:linear-gradient(135deg,#6b6a55,#a99872 50%,#4f5a3d)"></div>
<div class="photo" role="img" aria-label="Photo of colourful buoys hanging on a wooden wall" style="left:452px;top:3348px;width:301px;height:195px;background:linear-gradient(90deg,#5a4a42,#c9b9a8 30%,#b4453c 55%,#6b5a50)"></div>
<div class="photo" role="img" aria-label="Photo of a reel resting in green grass" style="left:784px;top:3348px;width:301px;height:195px;background:linear-gradient(135deg,#3f6b2e,#8fae5a 50%,#2f5222)"></div>
<svg class="abs" style="left:46px;top:3420px" width="26" height="50"><path d="M22 4L4 25l18 21" fill="none" stroke="#555" stroke-width="2.5"/></svg>
<svg class="abs" style="left:1128px;top:3420px" width="26" height="50"><path d="M4 4l18 21L4 46" fill="none" stroke="#555" stroke-width="2.5"/></svg>

<!-- footer -->
<svg class="abs" style="left:0;top:3630px" width="1200" height="480" viewBox="0 0 1200 480" preserveAspectRatio="none">
  <path d="M0 20 C250 60 450 70 700 40 C900 15 1050 0 1200 10 L1200 480 L0 480Z" fill="var(--dark)"/>
</svg>
<span class="abs" style="left:112px;top:3842px;width:10px;height:10px;border-radius:50%;background:#fff"></span>
<div class="abs" style="left:112px;top:3860px;font-size:28px;font-weight:600;color:#fff">tide-LOOP.</div>

<div class="foot-h" style="left:367px">QUICK LINKS</div>
<ul class="foot-links">
  <li>Home</li><li>About Us</li><li>Blog</li><li>Articles</li><li>Contact Us</li>
</ul>

<div class="foot-h" style="left:562px">CONTACT US</div>
<div class="f-row" style="top:3803px"><span class="ico"><svg width="14" height="18" viewBox="0 0 14 18"><path d="M7 1a6 6 0 016 6c0 4-6 10-6 10S1 11 1 7a6 6 0 016-6z" fill="#fff"/><circle cx="7" cy="7" r="2" fill="#333"/></svg></span><div><b>TIDE-LOOP.</b><br>Enim ad minima<br>veniam, quis nostrum.</div></div>
<div class="f-row" style="top:3882px"><span class="ico"><svg width="10" height="16"><rect x="1" y="1" width="8" height="14" rx="1.5" fill="none" stroke="#fff" stroke-width="1.6"/></svg></span><div><b>PHONE:</b><br>180 555 0142</div></div>
<div class="f-row" style="top:3940px"><span class="ico"><svg width="16" height="12"><rect x="1" y="1" width="14" height="10" fill="none" stroke="#fff" stroke-width="1.5"/><path d="M1 1l7 5 7-5" fill="none" stroke="#fff" stroke-width="1.5"/></svg></span><div><b>Mail:</b><br>info@tideloop.example</div></div>

<div class="foot-h" style="left:830px">NEWSLETTER SIGNUP</div>
<div class="field" style="left:830px;top:3800px;width:132px">Name</div>
<div class="field" style="left:968px;top:3800px;width:132px">Phone</div>
<div class="field" style="left:830px;top:3845px;width:270px">Email Address</div>
<a class="btn primary" href="#" style="left:830px;top:3898px;width:120px;height:38px;font-size:12px;font-weight:600">SIGNUP NOW</a>

<div class="abs" style="left:112px;top:4028px;width:976px;height:1px;background:rgba(255,255,255,.5)"></div>
<div class="abs" style="left:112px;top:4060px;font-size:14px;color:#fff">Copyright © 2018 tide-LOOP. All Rights Reserved.</div>
<a class="social" href="#" aria-label="Social link" style="left:896px"></a>
<a class="social" href="#" aria-label="Social link" style="left:934px"></a>
<a class="social" href="#" aria-label="Social link" style="left:972px"></a>
<a class="social" href="#" aria-label="Social link" style="left:1010px"></a>
<a class="social" href="#" aria-label="Social link" style="left:1048px"></a>

</body>
</html>
```